Meadowlark Dental Letterhead

Please design full color letterhead for meadowlark dental. Letterhead should match the motif of the business card. Print and logo should be confined to a one inch margin on top and bottom. The following info should be included:
Meadowlrk Dental with the tooth logo
Curtis R. Holloway, DDS
Gentle Hands, Bright Smiles Daily
Phone #: 918.555.0147
Address: 24813-C N Sycamore, Bixby, OK

```html
<!DOCTYPE html>
<html lang="en">
<head>
<meta charset="utf-8">
<title>Meadowlark Dental Letterhead</title>
<link href="https://fonts.googleapis.com/css2?family=Montserrat:wght@400;600;700;800&display=swap" rel="stylesheet">
<style>
  :root {
    --brand-blue: #2356a8;
    --brand-navy: #1d3f8c;
    --brand-red: #e2343b;
    --brand-green: #4dba3a;
    --brand-green-light: #7ed348;
    --ink-grey: #555b66;
    --paper: #ffffff;
  }
  html, body {
    margin: 0;
    padding: 0;
    overflow: hidden;
    background: var(--paper);
  }
  .letterhead {
    position: relative;
    width: 849px;
    height: 1200px;
    background: var(--paper);
    overflow: hidden;
    font-family: "Montserrat", sans-serif;
  }
  .brand {
    position: absolute;
    left: 74px;
    top: 62px;
    display: flex;
    align-items: center;
    gap: 14px;
  }
  .brand-mark {
    width: 46px;
    height: 46px;
    border-radius: 50%;
    background: var(--brand-blue);
    flex-shrink: 0;
  }
  .brand-text {
    display: flex;
    flex-direction: column;
  }
  .brand-name {
    font-weight: 800;
    font-size: 30px;
    line-height: 1;
    color: var(--brand-blue);
    letter-spacing: 0.5px;
    text-transform: uppercase;
  }
  .brand-tagline {
    margin-top: 6px;
    font-weight: 600;
    font-size: 9px;
    letter-spacing: 0.6px;
    color: var(--brand-navy);
    text-transform: uppercase;
  }
  .contact {
    position: absolute;
    left: 596px;
    top: 996px;
    color: var(--ink-grey);
  }
  .contact-name {
    font-weight: 700;
    font-size: 14px;
    color: var(--brand-navy);
    margin: 0 0 12px;
  }
  .contact-phone {
    display: flex;
    align-items: center;
    gap: 5px;
    margin-left: 48px;
    font-weight: 600;
    font-size: 11px;
    color: var(--brand-navy);
  }
  .contact-phone svg { width: 13px; height: 13px; }
  .contact-address {
    margin: 4px 0 0 48px;
    font-size: 8.5px;
    line-height: 1.4;
    font-style: normal;
  }
  .footer-rule {
    position: absolute;
    left: 0;
    width: 849px;
  }
  .footer-rule--red {
    top: 1118px;
    height: 4px;
    background: var(--brand-red);
  }
  .footer-rule--blue {
    top: 1126px;
    height: 6px;
    background: var(--brand-blue);
  }
  .footer-bar {
    position: absolute;
    left: 0;
    top: 1138px;
    width: 849px;
    height: 62px;
    background: linear-gradient(90deg, var(--brand-green-light), var(--brand-green));
  }
  .footer-slogan {
    position: absolute;
    right: 44px;
    top: 1159px;
    font-weight: 400;
    font-size: 16px;
    color: #ffffff;
    letter-spacing: 0.3px;
  }
</style>
</head>
<body>
<main class="letterhead">
  <header class="brand">
    <span class="brand-mark"></span>
    <div class="brand-text">
      <span class="brand-name">Meadowlark Dental</span>
      <span class="brand-tagline">Gentle Hands, Bright Smiles Daily</span>
    </div>
  </header>

  <section class="contact">
    <p class="contact-name">Curtis R. Holloway, D.D.S.</p>
    <div class="contact-phone">
      <svg viewBox="0 0 24 24" aria-hidden="true"><path fill="#1d3f8c" d="M6.6 10.8a15.1 15.1 0 0 0 6.6 6.6l2.2-2.2c.3-.3.7-.4 1-.2 1.1.4 2.3.6 3.6.6.6 0 1 .4 1 1V20c0 .6-.4 1-1 1A17 17 0 0 1 3 4c0-.6.4-1 1-1h3.5c.6 0 1 .4 1 1 0 1.3.2 2.5.6 3.6.1.3 0 .7-.2 1z"/></svg>
      <span>918.555.0147</span>
    </div>
    <address class="contact-address">
      24813-C N Sycamore<br>
      Willowcrest, OK 74120<br>
      www.meadowlarkdental.com
    </address>
  </section>

  <div class="footer-rule footer-rule--red"></div>
  <div class="footer-rule footer-rule--blue"></div>
  <div class="footer-bar"></div>
  <div class="footer-slogan">Care For Every Smile You Have</div>
</main>
</body>
</html>
```